New Business Card Design Project

Make a kick ass business card for The Otter Tea Mug, using the designs. I also might like the 2nd place design logo on the back? Maybe all black with that? Not sure. Also, I'm cool with it being on metal, plastic, glass? or whatever for the business card. Maybe shaped like a shark? Let me know what else you need? Would like designs in the next day or so. Thank you.
Target Market(s)
Anyone that is cool
Contact Information for Business Card
Name: Dorian Fenwick
Phone: 317.555.0126
inventor/creator/entrepreneur/owner
www.theottertyeamug.example
social media links
https://www.friendspace.example/theottertyeamug
https://chirper.example/otter_brew
https://www.snapgallery.example/theottertyeamug/
I'll get the Pinterest one soon
Colors
Designer to choose colors to be used in the design.
Requirements
Must have
- The Otter Tea Mug
- www.theottertyeamug.example
- social media tags?
- My logos and picture/photo of wine glass
Nice to have
- Maybe shaped like a wine glass or shark
- I'll let you decide but my same colors from my website would be nice

```html
<!DOCTYPE html>
<html lang="en">
<head>
<meta charset="utf-8">
<title>Otter Tea Mug — Business Card</title>
<link rel="stylesheet" href="https://fonts.googleapis.com/css2?family=Didact+Gothic&display=swap">
<style>
  :root {
    --ink: #060606;
    --panel-dark: #0d0d0d;
    --panel-mid: #1e1e1e;
    --panel-light: #2c2c2c;
    --text: #f2f2f2;
    --text-soft: #d6d6d6;
    --mark: #8a8a8a;
  }
  * { margin: 0; padding: 0; box-sizing: border-box; }
  html, body {
    width: 1200px;
    height: 686px;
    overflow: hidden;
    background: var(--ink);
  }
  .card {
    position: relative;
    width: 1200px;
    height: 686px;
    background: var(--ink);
    font-family: "Didact Gothic", sans-serif;
    color: var(--text);
    overflow: hidden;
  }
  .card__side-art {
    position: absolute;
    left: 640px;
    top: 0;
    width: 560px;
    height: 686px;
    background: linear-gradient(90deg, rgba(6,6,6,0) 0%, var(--panel-dark) 25%, var(--panel-mid) 60%, var(--panel-light) 100%);
  }
  .card__product-photo {
    position: absolute;
    left: 949px;
    top: 10px;
    width: 240px;
    height: 584px;
    border-radius: 120px 120px 40px 40px;
    background: radial-gradient(ellipse at 50% 30%, rgba(120,120,120,0.3), rgba(40,40,40,0.12) 60%, rgba(0,0,0,0) 80%);
  }
  .brand-mark {
    position: absolute;
    left: 154px;
    top: 76px;
    width: 326px;
    text-align: center;
    font-size: 26px;
    letter-spacing: 2px;
    color: var(--mark);
  }
  .brand-name {
    position: absolute;
    left: 78px;
    top: 164px;
    font-size: 55px;
    font-weight: 400;
    letter-spacing: 2px;
    color: var(--text);
  }
  .person__name {
    position: absolute;
    left: 80px;
    top: 254px;
    font-size: 39px;
    letter-spacing: 1.5px;
    color: var(--text);
  }
  .person__role {
    position: absolute;
    left: 80px;
    top: 298px;
    font-size: 23px;
    letter-spacing: 1px;
    color: var(--text-soft);
  }
  .contacts {
    position: absolute;
    left: 78px;
    top: 412px;
    list-style: none;
  }
  .contacts__item {
    display: flex;
    align-items: center;
    height: 42.5px;
    font-size: 23px;
    letter-spacing: 1px;
    color: var(--text);
  }
  .contacts__icon {
    width: 34px;
    height: 34px;
    margin-right: 17px;
    flex: none;
  }
</style>
</head>
<body>
<main class="card">
  <div class="card__side-art" role="img" aria-label="Decorative dark metallic side panel"></div>
  <div class="card__product-photo" role="img" aria-label="Photo of the product glass on a dark background"></div>

  <div class="brand-mark">Otter Tea Mug</div>
  <h1 class="brand-name">Otter Tea Mug</h1>

  <p class="person__name">Dorian Fenwick</p>
  <p class="person__role">inventor/creator/entrepreneur/owner</p>

  <ul class="contacts">
    <li class="contacts__item">
      <svg class="contacts__icon" viewBox="0 0 34 34" aria-hidden="true">
        <path d="M8 4 L13 4 L15 11 L11.5 14 C13 18 16 21 20 22.5 L23 19 L30 21 L30 26 C30 28 28 30 26 30 C15 29 5 19 4 8 C4 6 6 4 8 4 Z" fill="var(--text)"/>
      </svg>
      317.555.0126
    </li>
    <li class="contacts__item">
      <svg class="contacts__icon" viewBox="0 0 34 34" aria-hidden="true">
        <circle cx="17" cy="17" r="13" fill="none" stroke="var(--text)" stroke-width="3"/>
        <path d="M4 17 H30 M17 4 C10 10 10 24 17 30 M17 4 C24 10 24 24 17 30" fill="none" stroke="var(--text)" stroke-width="2"/>
      </svg>
      www.theottertyeamug.example
    </li>
    <li class="contacts__item">
      <svg class="contacts__icon" viewBox="0 0 34 34" aria-hidden="true">
        <rect x="3" y="3" width="28" height="28" rx="3" fill="var(--text)"/>
      </svg>
      https://www.friendspace.example/theottertyeamug
    </li>
    <li class="contacts__item">
      <svg class="contacts__icon" viewBox="0 0 34 34" aria-hidden="true">
        <circle cx="17" cy="17" r="13" fill="var(--text)"/>
      </svg>
      https://chirper.example/otter_brew
    </li>
    <li class="contacts__item">
      <svg class="contacts__icon" viewBox="0 0 34 34" aria-hidden="true">
        <rect x="4" y="4" width="26" height="26" rx="7" fill="none" stroke="var(--text)" stroke-width="3"/>
      </svg>
      https://www.snapgallery.example/theottertyeamug/
    </li>
  </ul>
</main>
</body>
</html>
```